Personal Business Card

I am an award winning banjo player who plays with two different professional bands. My experiences include studio recordings for other artists and played the theme song for the Creature Channel's "Frontier Tundra Nights". I am ready to take my career to the next level and would like something that will look professional. it is important to me to have a banjo on the card. If possible my accomplishments to be put on back of card.

Industry/Entity Type

Artists

Contact Information for Business Card

Morgan Pell
cell 602-315-2860
email morganpellbanjo@quillpost.net

2008 AZ Banjo Champion
2008 Pinemeadow Banjo Champion
2010 AZ Banjo Champion
2010 Copper Creek Gathering Halvorn Banjo Champion
2010 Birchstone Hollow Fair Banjo Finalist

```html
<!DOCTYPE html>
<html lang="en">
<head>
<meta charset="utf-8">
<title>Morgan Pell — Business Card</title>
<link rel="stylesheet" href="https://fonts.googleapis.com/css2?family=Open+Sans:wght@400;600;700&display=swap">
<style>
  :root {
    --page: #e9e7e4;
    --card-dark: #2c2c2e;
    --card-light: #ffffff;
    --accent: #f5ad1b;
    --tag-grey: #d8d8d8;
    --ink-dark: #262626;
    --ink-light: #f2f2f2;
    --ink-muted: #cfcfcf;
  }
  * { box-sizing: border-box; margin: 0; padding: 0; }
  html, body { width: 1200px; height: 900px; overflow: hidden; }
  body {
    background: var(--page);
    font-family: "Open Sans", Arial, sans-serif;
    display: flex;
    align-items: center;
    justify-content: center;
    gap: 40px;
  }
  .card {
    position: relative;
    width: 540px;
    height: 309px;
    overflow: hidden;
    box-shadow: 0 10px 28px rgba(0,0,0,0.18);
  }
  .card svg.card-shapes { position: absolute; inset: 0; }

  /* Back card */
  .card--back { background: var(--card-dark); }
  .honours {
    position: absolute;
    top: 34px;
    left: 34px;
    list-style: none;
    color: var(--ink-light);
    font-size: 15.5px;
    line-height: 1.5;
    font-weight: 400;
  }
  .name-mark {
    position: absolute;
    display: flex;
    align-items: center;
    gap: 9px;
    color: var(--ink-dark);
    font-weight: 600;
    font-size: 22px;
    letter-spacing: 0.2px;
  }
  .name-mark__dot {
    width: 13px; height: 13px;
    border-radius: 50%;
    background: var(--ink-dark);
  }
  .card--back .name-mark { top: 202px; left: 268px; }

  /* Front card */
  .card--front { background: var(--card-light); }
  .banjo-art {
    position: absolute;
    top: 22px;
    left: 70px;
    width: 330px;
    height: 180px;
    border-radius: 90px 30px 30px 90px;
    background: radial-gradient(circle at 28% 50%, #f4f4f4 0%, #dcdcdc 38%, #bdbdbd 45%, #ececec 60%, #f7f7f7 100%);
  }
  .card--front .name-mark { top: 162px; left: 368px; font-size: 21px; }
  .contact {
    position: absolute;
    left: 30px;
    top: 244px;
    list-style: none;
    color: var(--ink-muted);
    font-size: 12.5px;
    line-height: 1.75;
  }
  .contact li { display: flex; align-items: center; gap: 8px; }
  .contact svg { width: 12px; height: 12px; flex: none; }
</style>
</head>
<body>

  <section class="card card--back" aria-label="Card back: accomplishments">
    <svg class="card-shapes" viewBox="0 0 540 309" aria-hidden="true">
      <path d="M262 188 H540 V244 H262 L250 232 V200 Z" fill="var(--accent)"/>
    </svg>
    <ul class="honours">
      <li>2008 AZ Banjo Champion</li>
      <li>2008 Pinemeadow Banjo Champion</li>
      <li>2010 AZ Banjo Champion</li>
      <li>2010 Copper Creek Gathering Halvorn Banjo Champion</li>
      <li>2010 Birchstone Hollow Fair Banjo Finalist</li>
    </ul>
    <div class="name-mark"><span class="name-mark__dot"></span><span>Morgan Pell</span></div>
  </section>

  <section class="card card--front" aria-label="Card front: contact details">
    <div class="banjo-art" role="img" aria-label="Banjo illustration lying diagonally across the card"></div>
    <svg class="card-shapes" viewBox="0 0 540 309" aria-hidden="true">
      <path d="M350 150 H540 V202 H350 L338 190 V162 Z" fill="var(--tag-grey)"/>
      <path d="M0 226 H318 Q338 226 346 244 L374 309 H0 Z" fill="var(--card-dark)"/>
      <path d="M362 236 H430 L470 309 H392 Z" fill="var(--accent)"/>
    </svg>
    <div class="name-mark"><span class="name-mark__dot"></span><span>Morgan Pell</span></div>
    <ul class="contact">
      <li>
        <svg viewBox="0 0 12 12" aria-hidden="true"><path d="M2.5 1 L4.5 1 L5.3 3.4 L4 4.3 Q5 6.6 7.7 8 L8.6 6.7 L11 7.5 V9.5 Q11 11 9.5 11 Q1 10.5 1 2.5 Q1 1 2.5 1 Z" fill="var(--ink-muted)"/></svg>
        <span>602-315-2860</span>
      </li>
      <li>
        <svg viewBox="0 0 12 12" aria-hidden="true"><rect x="0.75" y="2.25" width="10.5" height="7.5" fill="none" stroke="var(--ink-muted)" stroke-width="1.2"/><path d="M1 2.6 L6 6.6 L11 2.6" fill="none" stroke="var(--ink-muted)" stroke-width="1.2"/></svg>
        <span>morganpellbanjo@quillpost.net</span>
      </li>
    </ul>
  </section>

</body>
</html>
```